Diesel Fitting/Mechanical Company Needs a new Business Card

We would like a new business card that showcases our logo and business information.

Industry/Entity Type

Business

Contact Information for Business Card

314 Wendale Street
PO Box 7581 CARLTON DOWNS QLD 4836
Phone: 49312787 Fax: 49312688 Mobile: 0438915276 ABN: 63 519 087 342

Requirements
Must have
• The following email addresses:
• admin@tkservicing.com.au , sales@tkservicing.com.au , accounts@tkservicing.com.au , parts@tkservicing.com.au , office@tkservicing.com.au
• Also need to have the website: www.tkservicing.com.au

```html
<!DOCTYPE html>
<html lang="en">
<head>
<meta charset="utf-8">
<title>TK Servicing — Business Card</title>
<link rel="stylesheet" href="https://fonts.googleapis.com/css2?family=Questrial&family=Roboto+Condensed:wght@700&display=swap">
<style>
  :root {
    --backdrop: #5b4a3b;
    --card-white: #f1f1f1;
    --card-black: #050505;
    --brand-orange: #f47a20;
    --ink-dark: #1a1a1a;
    --ink-light: #f4f4f4;
    --ink-muted: #6e6e6e;
    --brand-faint: #ecd9cc;
  }
  * { margin: 0; padding: 0; box-sizing: border-box; }
  html, body { width: 1200px; height: 960px; overflow: hidden; }
  body {
    background: var(--backdrop);
    position: relative;
    font-family: "Questrial", "Century Gothic", sans-serif;
  }
  .card {
    position: absolute;
    width: 600px;
    height: 343px;
    background: var(--card-white);
    overflow: hidden;
  }
  .card--front { left: 314px; top: 113px; }
  .card--back { left: 311px; top: 472px; }

  .front__stripe {
    position: absolute; left: 0; top: 0; width: 16px; height: 100%;
    background: var(--brand-orange);
  }
  .front__identity {
    position: absolute; left: 16px; top: 0; width: 292px; height: 100%;
    text-align: center;
  }
  .brand {
    position: absolute; left: 0; right: 0; top: 120px;
    display: flex; align-items: center; justify-content: center; gap: 10px;
  }
  .brand__dot {
    width: 18px; height: 18px; border-radius: 50%;
    background: var(--brand-orange);
  }
  .brand__name {
    font-size: 34px; color: var(--brand-orange); line-height: 1;
  }
  .person {
    position: absolute; left: 0; right: 0; top: 234px;
  }
  .person__name {
    font-family: "Roboto Condensed", "Arial Narrow", sans-serif;
    font-weight: 700; font-size: 23px; color: var(--brand-orange);
    letter-spacing: 0.5px; line-height: 1;
  }
  .person__role {
    margin-top: 5px; font-size: 15px; color: var(--ink-dark);
  }

  .front__contact {
    position: absolute; left: 308px; top: 0; right: 0; height: 100%;
    background: var(--card-black);
    color: var(--ink-light);
    padding: 55px 0 0 35px;
  }
  .contact-list { list-style: none; }
  .contact-list li {
    display: flex; align-items: center; gap: 8px;
    font-size: 15.5px; height: 19px; line-height: 19px;
  }
  .contact-list svg { width: 14px; height: 14px; flex: none; fill: var(--brand-orange); }
  .address {
    margin-top: 10px; font-size: 15.5px; line-height: 18px; font-style: normal;
  }

  .back__brand {
    position: absolute; left: 0; right: 0; top: 130px;
    display: flex; align-items: center; justify-content: center; gap: 16px;
  }
  .back__brand .brand__dot { width: 30px; height: 30px; background: var(--brand-faint); }
  .back__brand .brand__name { font-size: 64px; color: var(--brand-faint); }
  .back__web {
    position: absolute; left: 0; right: 0; top: 293px;
    text-align: center; font-size: 15.5px; letter-spacing: 3px; color: var(--ink-muted);
  }
</style>
</head>
<body>

<section class="card card--front">
  <div class="front__stripe"></div>
  <div class="front__identity">
    <div class="brand">
      <span class="brand__dot"></span>
      <span class="brand__name">TK Servicing</span>
    </div>
    <div class="person">
      <div class="person__name">DANIEL HARTLEY</div>
      <div class="person__role">CEO/FOUNDER</div>
    </div>
  </div>
  <div class="front__contact">
    <ul class="contact-list">
      <li><svg viewBox="0 0 16 16"><path d="M3.5 1l3 3-1.8 1.8c.9 2 2.5 3.6 4.5 4.5L11 8.5l3 3-2 2.5C6.5 13.5 2.5 9.5 1 4z"/></svg>49312787</li>
      <li><svg viewBox="0 0 16 16"><path d="M4 1h8v14H4zM5.5 3v9h5V3zM7 13h2v1H7z" fill-rule="evenodd"/></svg>49312688</li>
      <li><svg viewBox="0 0 16 16"><path d="M4 2h7v3H4zM1 6h14v7h-2v-3H3v3H1zM4 11h8v4H4z"/></svg>0438915276</li>
      <li><svg viewBox="0 0 16 16"><path d="M1 4h14v9H1zM2 5l6 4 6-4" stroke="#050505" stroke-width="1"/></svg>admin@tkservicing.com.au</li>
      <li><svg viewBox="0 0 16 16"><path d="M1 4h14v9H1zM2 5l6 4 6-4" stroke="#050505" stroke-width="1"/></svg>sales@tkservicing.com.au</li>
      <li><svg viewBox="0 0 16 16"><path d="M1 4h14v9H1zM2 5l6 4 6-4" stroke="#050505" stroke-width="1"/></svg>accounts@tkservicing.com.au</li>
      <li><svg viewBox="0 0 16 16"><path d="M1 4h14v9H1zM2 5l6 4 6-4" stroke="#050505" stroke-width="1"/></svg>parts@tkservicing.com.au</li>
      <li><svg viewBox="0 0 16 16"><path d="M1 4h14v9H1zM2 5l6 4 6-4" stroke="#050505" stroke-width="1"/></svg>office@tkservicing.com.au</li>
      <li><svg viewBox="0 0 16 16"><circle cx="8" cy="8" r="7"/><path d="M4 5c2 0 2 2 4 2s1 3-1 3-1 3-2 4M10 2c0 2 2 2 3 3" stroke="#050505" stroke-width="1.2" fill="none"/></svg>www.tkservicing.com.au</li>
    </ul>
    <address class="address">
      314 Wendale Street<br>
      PO Box 7581 CARLTON DOWNS<br>
      QLD 4836
    </address>
  </div>
</section>

<section class="card card--back">
  <div class="back__brand">
    <span class="brand__dot"></span>
    <span class="brand__name">TK Servicing</span>
  </div>
  <div class="back__web">www.tkservicing.com.au</div>
</section>

</body>
</html>
```